Warranty Card Design for Mattress Brand

We would like to design a warranty card for our mattresses,
it consists of 2 pages in one card (front and back) to be neatly showing our warranty details/text , our logo , our website, address and telephone clearly.

Target Market(s)

household

Font styles to use
Serif
Script

Colors
3277b5
33a6d7
85cae6
0492cd
3176b5
0355a3
85abd2
cee9f5
85acd3

Requirements
Must have
• a nice warranty logo
Nice to have
• a nice warranty logo with a neat text and clear layout, colors have to be related to the logo

```html
<!DOCTYPE html>
<html lang="en">
<head>
<meta charset="utf-8">
<title>Dreamloft Warranty Card</title>
<link rel="stylesheet" href="https://fonts.googleapis.com/css2?family=Roboto:wght@300;400;500&family=PT+Sans:wght@400&family=Roboto+Condensed:wght@700&display=swap">
<style>
  :root {
    --stage: #c6c6c6;
    --card: #cde9eb;
    --ink: #111111;
    --ink-soft: #2b2b2b;
    --brand-blue: #0355a3;
    --stamp-blue: #1d48a0;
    --band-blue: #5276bc;
    --band-edge: #3e3f44;
    --tick: #3176b5;
    --white: #ffffff;
  }
  * { box-sizing: border-box; margin: 0; padding: 0; }
  html, body { width: 1200px; height: 1200px; overflow: hidden; }
  body { background: var(--stage); font-family: "Roboto", Arial, sans-serif; color: var(--ink); position: relative; }

  .card {
    position: absolute; left: 102px; width: 1004px; height: 394px;
    background: var(--card); overflow: hidden;
  }
  .card--front { top: 134px; }
  .card--back { top: 632px; }

  .band { position: absolute; left: 863px; top: 0; width: 141px; height: 394px; }
  .band__name {
    position: absolute; left: 915px; top: 350px; color: var(--white);
    font-family: "Roboto", Arial, sans-serif; font-weight: 300; font-size: 34px; line-height: 40px;
    transform: rotate(-90deg); transform-origin: left top; white-space: nowrap;
  }
  .band__tag {
    position: absolute; left: 968px; top: 336px; color: var(--white);
    font-family: "PT Sans", Arial, sans-serif; font-size: 7.5px; line-height: 10px; letter-spacing: 1.8px;
    transform: rotate(-90deg); transform-origin: left top; white-space: nowrap;
  }

  .warranty-mark { position: absolute; display: flex; align-items: center; gap: 10px; }
  .warranty-mark__brand {
    font-family: "Roboto", Arial, sans-serif; font-weight: 300; font-size: 14px; color: var(--brand-blue);
  }
  .warranty-mark__word {
    font-family: "Roboto Condensed", Arial, sans-serif; font-weight: 700;
    font-size: 50px; color: var(--stamp-blue); line-height: 1; white-space: nowrap;
  }
  .warranty-mark--front { left: 352px; top: 32px; }
  .warranty-mark--side {
    left: -6px; top: 150px; width: 248px; height: 56px; justify-content: center;
    transform: rotate(-90deg); transform-origin: center;
  }
  .side-brand { position: absolute; left: 92px; top: 294px; }

  .copy { position: absolute; left: 44px; white-space: nowrap; }
  .copy h2 { font-size: 13px; font-weight: 500; line-height: 16px; margin-bottom: 1px; }
  .copy p { font-size: 11.6px; font-weight: 300; line-height: 15.3px; color: var(--ink-soft); }
  .copy .section + .section { margin-top: 14px; }

  .checklist { list-style: none; }
  .checklist li {
    position: relative; padding-left: 16px; font-size: 11.6px; line-height: 16.8px; color: var(--ink-soft);
  }
  .checklist--regular li { font-weight: 400; }
  .checklist--light li { font-size: 11.3px; font-weight: 300; line-height: 16.9px; }
  .checklist li::before {
    content: ""; position: absolute; left: 0; top: 4px; width: 9px; height: 9px;
    border: 1px solid var(--tick);
  }
  .checklist li::after {
    content: ""; position: absolute; left: 3px; top: 5px; width: 3px; height: 5px;
    border: solid var(--tick); border-width: 0 1.3px 1.3px 0; transform: rotate(40deg);
  }
  .checklist .wrap { display: inline-block; padding-left: 3px; line-height: 15.2px; }

  .fields { position: absolute; left: 44px; top: 317px; display: flex; gap: 20px; font-size: 12.8px; white-space: nowrap; }
  .field { display: flex; align-items: flex-end; gap: 5px; }
  .field__line { display: inline-block; border-bottom: 1px solid var(--ink); height: 13px; }

  .contact {
    position: absolute; left: 44px; top: 352px; display: flex; align-items: center;
    font-family: "PT Sans", Arial, sans-serif; font-size: 13.8px; white-space: nowrap;
  }
  .contact__company { font-family: "Roboto", Arial, sans-serif; font-weight: 500; font-size: 13.3px; }
  .contact__sep { margin: 0 10px; }
  .contact__item { display: flex; align-items: center; gap: 3px; margin-left: 19px; }
  .contact__sep + .contact__item { margin-left: 0; }
  .contact svg { width: 14px; height: 14px; }
</style>
</head>
<body>

<section class="card card--front" aria-label="Warranty card front">
  <div class="warranty-mark warranty-mark--front">
    <span class="warranty-mark__brand">Dreamloft</span>
    <span class="warranty-mark__word">WARRANTY</span>
  </div>

  <div class="copy" style="top:100px;">
    <h2>Congratulations on your new DREAMLOFT mattress.</h2>
    <p>We always strive to provide you with the most comfortable and healthy sleep by offering you the highest product quality and durability.<br>
    Our company was awarded the ISO 9001 accreditation certificate for the quality of its Mattress Production.<br>
    By implementing the ISO 9001 quality management system, we assure our customers that the products and the services we provide will meet their expectations.<br>
    Our products are guaranteed against defects in workmanship and material. In case of defect, we shall repair or replace, at our discretion, the defective component.<br>
    Pease keep this card in a safe place. Should you face any problems, please contact our service department</p>
  </div>

  <div class="copy" style="top:202px;">
    <h2 style="font-size:12px;">To ensure you get maximum comfort and support, please follow the following instructions:</h2>
    <ul class="checklist checklist--regular">
      <li>Make sure the bed base foundation is in good condition and well ventilated.</li>
      <li>Turn/Flip your mattress every 3 months to maximize its comfort and lifespan.</li>
      <li>Avoid exposing the mattress to the sun; air it in a passage area instead.</li>
      <li>In case of possibility of liquids dripping on the mattress, consider covering it with a mattress protection pad.</li>
      <li>Do not worry if the mattress feels slightly firmer than anticipated within weeks of usage, the interior will soften and initial stiffness will be removed.</li>
    </ul>
  </div>

  <div class="fields">
    <div class="field">Invoice Number <span class="field__line" style="width:205px"></span></div>
    <div class="field">Warranty Period <span class="field__line" style="width:205px"></span></div>
    <div class="field">Date <span class="field__line" style="width:128px"></span></div>
  </div>

  <div class="contact">
    <span class="contact__company">Haddad Bedding Co.</span>
    <span class="contact__sep">|</span>
    <span class="contact__item">Cedar Park, Factory Lane, Zahle, Lebanon</span>
    <span class="contact__item">
      <svg viewBox="0 0 14 14"><path d="M9 1.5C5 2.5 3 7 4.5 12l2-1C5.5 8 6.5 5 9.5 4Z" fill="none" stroke="#3176b5" stroke-width="1.3"/></svg>+961 1 555 010</span>
    <span class="contact__item">
      <svg viewBox="0 0 14 14"><g fill="none" stroke="#3176b5" stroke-width="1"><circle cx="7" cy="7" r="5.8"/><ellipse cx="7" cy="7" rx="2.6" ry="5.8"/><path d="M1.2 7h11.6M2 4h10M2 10h10"/></g></svg>&nbsp;www.haddadbedding.com</span>
  </div>

  <svg class="band" viewBox="0 0 141 394" aria-hidden="true">
    <path d="M0 394C3 250 45 140 141 58V394Z" fill="var(--band-edge)"/>
    <path d="M17 394C20 260 60 150 141 74V394Z" fill="var(--band-blue)"/>
  </svg>
  <span class="band__name">Dreamloft</span>
  <span class="band__tag">MATTRESSES &amp; PILLOWS</span>
</section>

<section class="card card--back" aria-label="Warranty card back">
  <div class="warranty-mark warranty-mark--side">
    <span class="warranty-mark__word">WARRANTY</span>
  </div>
  <span class="warranty-mark__brand side-brand">Dreamloft</span>

  <div class="copy" style="left:211px; top:42px;">
    <div class="section">
      <h2>This limited Mattress Warranty applies to the following Defects:</h2>
      <ul class="checklist checklist--light">
        <li>Coils or wires that are broken or piercing through fabric.</li>
        <li>Sagging, that measures 3cm or greater (being properly measured) only if the mattress has been continuously supported by<br><span class="wrap">appropriate and solid foundation</span></li>
      </ul>
    </div>
    <div class="section">
      <h2>This limited Mattress Warranty does not cover the following:</h2>
      <ul class="checklist checklist--light">
        <li>Comfort preference</li>
        <li>Fabric Stains, soiling or burns</li>
        <li>Body impressions of less than 3cm</li>
        <li>Damage to the mattress due to abuse</li>
        <li>Bent Perimeter border rods due to moving or bending the mattress</li>
        <li>Size allowance of +/- 2cm</li>
        <li>Bed Bugs and Dust Mites</li>
        <li>Mattress Odor: as in any upholstery, new mattress may have odor that will fade with time</li>
        <li>For Latex and Memory Foam mattresses: normal change in softness and recovery time in these materials with time. This does<br><span class="wrap">not affect the relieving qualities of these mattresses.</span></li>
        <li>Transportation and Inspection Costs</li>
      </ul>
    </div>
  </div>

  <div class="contact">
    <span class="contact__company">Haddad Bedding Co.</span>
    <span class="contact__sep">|</span>
    <span class="contact__item">Cedar Park, Factory Lane, Zahle, Lebanon</span>
    <span class="contact__item">
      <svg viewBox="0 0 14 14"><path d="M9 1.5C5 2.5 3 7 4.5 12l2-1C5.5 8 6.5 5 9.5 4Z" fill="none" stroke="#3176b5" stroke-width="1.3"/></svg>+961 1 555 010</span>
    <span class="contact__item">
      <svg viewBox="0 0 14 14"><g fill="none" stroke="#3176b5" stroke-width="1"><circle cx="7" cy="7" r="5.8"/><ellipse cx="7" cy="7" rx="2.6" ry="5.8"/><path d="M1.2 7h11.6M2 4h10M2 10h10"/></g></svg>&nbsp;www.haddadbedding.com</span>
  </div>

  <svg class="band" viewBox="0 0 141 394" aria-hidden="true">
    <path d="M0 394C3 250 45 140 141 58V394Z" fill="var(--band-edge)"/>
    <path d="M17 394C20 260 60 150 141 74V394Z" fill="var(--band-blue)"/>
  </svg>
  <span class="band__name">Dreamloft</span>
  <span class="band__tag">MATTRESSES &amp; PILLOWS</span>
</section>

</body>
</html>
```